We sell companies excess stock for them

We need a business card for a company based in New Zealand called 'StockHarbor'.

Check out our website to get an idea www.stockharbor.example

We help other businesses to;
- Sell Excess Stock
- Manage Product Returns
- Sell Company Assets

Our logo is attached for your reference
The font used is 'RifficFree-Bold'

Target Market(s)

Businesses

Industry/Entity Type

Business

Contact Information for Business Card

Name: Mark Pellow
Phone: 027 846 2093
email: markpellow@stockharbor.example
website: www.stockharbor.example

Font styles to use
Other font styles liked:
• Unsure

Colors
9bcb3b

Requirements
Must have
• coming soon
Nice to have
• coming soon
Should not have
• coming soon

```html
<!DOCTYPE html>
<html lang="en">
<head>
<meta charset="utf-8">
<title>StockHarbor Business Card</title>
<link rel="stylesheet" href="https://fonts.googleapis.com/css2?family=Fredoka:wght@600;700&family=Figtree:wght@400;500&display=swap">
<style>
  :root {
    --stage: #c8c8c8;
    --card-dark-top: #3b3c3e;
    --card-dark-bottom: #2b2c2e;
    --card-light-top: #f4f4f4;
    --card-light-bottom: #e4e4e4;
    --brand-green: #9bcb3b;
    --band-green: #8cbc2c;
    --ink-dark: #3a3a3a;
    --ink-text: #2e2e2e;
    --ink-muted: #555555;
    --white: #f2f2f2;
  }
  * { box-sizing: border-box; margin: 0; padding: 0; }
  html, body {
    width: 1200px;
    height: 576px;
    overflow: hidden;
    background: var(--stage);
  }
  .stage {
    position: relative;
    width: 1200px;
    height: 576px;
  }
  .card {
    position: absolute;
    top: 138px;
    width: 484px;
    height: 294px;
    border-radius: 14px;
    overflow: hidden;
  }
  /* Front */
  .card-front {
    left: 82px;
    background: linear-gradient(160deg, var(--card-dark-top) 0%, var(--card-dark-bottom) 100%);
  }
  .brand-mark {
    position: absolute;
    left: 50%;
    top: 62px;
    width: 96px;
    height: 96px;
    margin-left: -48px;
    border-radius: 50%;
    background: var(--brand-green);
  }
  .front-wordmark {
    position: absolute;
    left: 0;
    right: 0;
    top: 196px;
    text-align: center;
    font-family: "Fredoka", sans-serif;
    font-weight: 700;
    font-size: 35px;
    letter-spacing: -0.5px;
    color: var(--white);
  }
  .service-band {
    position: absolute;
    left: 0;
    right: 0;
    bottom: 0;
    height: 30px;
    background: var(--band-green);
    display: flex;
    align-items: center;
    justify-content: center;
    gap: 8px;
    font-family: "Figtree", sans-serif;
    font-weight: 500;
    font-size: 13.5px;
    color: var(--ink-text);
  }
  .service-divider { opacity: 0.8; }
  /* Back */
  .card-back {
    left: 602px;
    background: linear-gradient(170deg, var(--card-light-top) 0%, var(--card-light-bottom) 100%);
  }
  .back-wordmark {
    position: absolute;
    left: 0;
    right: 0;
    top: 92px;
    text-align: center;
    font-family: "Fredoka", sans-serif;
    font-weight: 700;
    font-size: 35px;
    letter-spacing: -0.5px;
    color: var(--ink-dark);
  }
  .person {
    position: absolute;
    right: 272px;
    top: 146px;
    text-align: right;
  }
  .person-name {
    font-family: "Fredoka", sans-serif;
    font-weight: 700;
    font-size: 22px;
    line-height: 1;
    color: var(--ink-dark);
  }
  .person-name .surname { color: var(--brand-green); }
  .person-title {
    margin-top: 5px;
    font-family: "Figtree", sans-serif;
    font-size: 10.5px;
    color: var(--ink-muted);
  }
  .contact-list {
    position: absolute;
    left: 236px;
    top: 147px;
    list-style: none;
    font-family: "Figtree", sans-serif;
    font-size: 13px;
    color: var(--ink-text);
  }
  .contact-item {
    display: flex;
    align-items: center;
    gap: 9px;
    height: 16.5px;
  }
  .contact-icon { width: 10px; height: 10px; flex: none; }
</style>
</head>
<body>
<main class="stage">
  <section class="card card-front" aria-label="Card front">
    <div class="brand-mark" aria-hidden="true"></div>
    <div class="front-wordmark">StockHarbor</div>
    <div class="service-band">
      <span>Sell Excess Stock</span>
      <span class="service-divider">|</span>
      <span>Manage Product Returns</span>
      <span class="service-divider">|</span>
      <span>Sell Company Assets</span>
    </div>
  </section>

  <section class="card card-back" aria-label="Card back">
    <div class="back-wordmark">StockHarbor</div>
    <div class="person">
      <div class="person-name">Mark <span class="surname">Pellow</span></div>
      <div class="person-title">Managing Director</div>
    </div>
    <ul class="contact-list">
      <li class="contact-item">
        <svg class="contact-icon" viewBox="0 0 10 10" aria-hidden="true">
          <path d="M1 3.2 Q5 0.6 9 3.2 L8 4.4 L6.6 3.6 L6.6 2.8 Q5 2.3 3.4 2.8 L3.4 3.6 L2 4.4 Z" fill="var(--brand-green)"/>
          <rect x="2" y="5" width="6" height="4" rx="0.8" fill="var(--brand-green)"/>
        </svg>
        <span>027 846 2093</span>
      </li>
      <li class="contact-item">
        <svg class="contact-icon" viewBox="0 0 10 10" aria-hidden="true">
          <rect x="0.5" y="2" width="9" height="6.5" fill="var(--brand-green)"/>
          <path d="M0.5 2 L5 5.6 L9.5 2" fill="none" stroke="#ffffff" stroke-width="0.9"/>
        </svg>
        <span>markpellow@stockharbor.example</span>
      </li>
      <li class="contact-item">
        <svg class="contact-icon" viewBox="0 0 10 10" aria-hidden="true">
          <circle cx="5" cy="5" r="4.3" fill="var(--brand-green)"/>
          <path d="M0.8 5 H9.2 M5 0.8 Q2.6 5 5 9.2 M5 0.8 Q7.4 5 5 9.2" fill="none" stroke="#ffffff" stroke-width="0.6"/>
        </svg>
        <span>www.stockharbor.example</span>
      </li>
    </ul>
  </section>
</main>
</body>
</html>
```